I need a newspaper ads that suits events / outings all over the world. refreshing feeling that suits my company logo.
Size of the ads is 6cm by 6cm a square
takenote
1) Joining up as members is free .
2) Places of interest tickets discount for members
3) Special events / outings host almost everyday
4) main point is everyone able to know each another
website : www.WanderNookly.com
Target Market(s)
Targeting general age 18-40 . mainly singles
contents to put inside the ads
2) Local Places of interest tickets discount for members
4) Website : www.WanderNookly.com
5) We also host photos contest
6) Meet the different faces of the world
7) Experience Sharing Gathering !
Industry/Entity Type
It Company
Requirements
Must have
- Refreshing feeling , and professional . will be uploading more pictures , kindly put some pictures combine into it to make people feel there is a lot activities can be involve when they join as member.

```html
<!DOCTYPE html>
<html lang="en">
<head>
<meta charset="utf-8">
<title>Nookly Events – Newspaper Ad</title>
<link rel="stylesheet" href="https://fonts.googleapis.com/css2?family=Oswald:wght@500&family=PT+Sans+Narrow&display=swap">
<style>
  :root {
    --board: #d9dadc;
    --paper: #ffffff;
    --ink: #3d3d3d;
    --blue-light: #27a8da;
    --blue-dark: #0b5a8c;
    --gray-light: #9a9a9a;
    --gray-dark: #444444;
  }
  * { margin: 0; padding: 0; box-sizing: border-box; }
  html, body { width: 1200px; height: 900px; overflow: hidden; background: var(--board); }
  .board { position: relative; width: 1200px; height: 900px; }

  .ad {
    position: absolute; top: 278px;
    width: 354px; height: 354px;
    background: var(--paper);
    transform: scale(0.968); transform-origin: top left;
    font-family: "PT Sans Narrow", "Arial Narrow", sans-serif;
    color: var(--ink);
    overflow: hidden;
  }
  .ad--colour { left: 243px; --accent-a: var(--blue-light); --accent-b: var(--blue-dark);
    --photo-a: #6f8f4e; --photo-b: #3f4a3a; --photo-c: #a9b99a; }
  .ad--mono { left: 615px; --accent-a: var(--gray-light); --accent-b: var(--gray-dark);
    --photo-a: #8a8a8a; --photo-b: #3e3e3e; --photo-c: #c4c4c4; }

  .photo {
    position: absolute; width: 101px; height: 101px;
    background: linear-gradient(160deg, var(--photo-c), var(--photo-a) 45%, var(--photo-b));
  }
  .photo--one { left: 15px; top: 18px; border-top-left-radius: 30px; }
  .photo--two { left: 127px; top: 18px; }
  .photo--three { left: 239px; top: 18px; border-top-right-radius: 30px; }
  .photo--four { left: 239px; top: 127px; border-bottom-right-radius: 30px; }

  .perks {
    position: absolute; left: 15px; top: 128px; width: 215px;
    list-style: none; font-size: 10.6px; line-height: 12px;
  }
  .perks li { margin-bottom: 6px; padding-left: 6px; text-indent: -6px; }
  .perks li::before { content: "• "; }

  .headline { position: absolute; left: 0; top: 240px; width: 354px; height: 100px; }
  .headline text { font-family: "Oswald", "Arial Narrow", sans-serif; font-weight: 500; font-size: 32px; }

  .site { position: absolute; left: 15px; top: 327px; font-size: 11.5px; }

  .brand { position: absolute; right: 14px; top: 316px; display: flex; align-items: center; gap: 8px; }
  .brand__dot { width: 30px; height: 30px; border-radius: 50%; background: var(--accent-b); }
  .brand__name { font-size: 17px; letter-spacing: 1px; color: var(--accent-b); }
</style>
</head>
<body>
<main class="board">

  <section class="ad ad--colour">
    <div class="photo photo--one" role="img" aria-label="Photo of members posing together outdoors"></div>
    <div class="photo photo--two" role="img" aria-label="Photo of a group of friends in a park"></div>
    <div class="photo photo--three" role="img" aria-label="Photo of members on an outing"></div>
    <div class="photo photo--four" role="img" aria-label="Photo of a member feeding a giraffe at the zoo"></div>
    <ul class="perks">
      <li>Joining up as members is free</li>
      <li>Local Places of interest tickets discount for members</li>
      <li>Special events / outings host almost everyday</li>
      <li>We also host photos contest</li>
      <li>Meet the different faces of the world</li>
      <li>Experience Sharing Gathering !</li>
    </ul>
    <svg class="headline" viewBox="0 0 354 100" aria-label="The gate to the new world">
      <defs>
        <linearGradient id="accent-colour" x1="0" x2="1">
          <stop offset="0" stop-color="var(--blue-light)"/><stop offset="1" stop-color="var(--blue-dark)"/>
        </linearGradient>
        <path id="arc-colour" d="M12,54 Q170,34 346,30"/>
      </defs>
      <text fill="url(#accent-colour)"><textPath href="#arc-colour" textLength="334">THE GATE TO THE NEW WORLD</textPath></text>
      <path d="M0,68 Q40,60 170,48 Q290,40 354,50 L354,53 Q290,44 170,53 Q60,62 0,74 Z" fill="url(#accent-colour)"/>
    </svg>
    <p class="site">www.WanderNookly.com</p>
    <div class="brand"><span class="brand__dot"></span><span class="brand__name">NOOKLY EVENTS</span></div>
  </section>

  <section class="ad ad--mono">
    <div class="photo photo--one" role="img" aria-label="Black and white photo of members posing together outdoors"></div>
    <div class="photo photo--two" role="img" aria-label="Black and white photo of a group of friends in a park"></div>
    <div class="photo photo--three" role="img" aria-label="Black and white photo of members on an outing"></div>
    <div class="photo photo--four" role="img" aria-label="Black and white photo of a member feeding a giraffe at the zoo"></div>
    <ul class="perks">
      <li>Joining up as members is free</li>
      <li>Local Places of interest tickets discount for members</li>
      <li>Special events / outings host almost everyday</li>
      <li>We also host photos contest</li>
      <li>Meet the different faces of the world</li>
      <li>Experience Sharing Gathering !</li>
    </ul>
    <svg class="headline" viewBox="0 0 354 100" aria-label="The gate to the new world">
      <defs>
        <linearGradient id="accent-mono" x1="0" x2="1">
          <stop offset="0" stop-color="var(--gray-light)"/><stop offset="1" stop-color="var(--gray-dark)"/>
        </linearGradient>
        <path id="arc-mono" d="M12,54 Q170,34 346,30"/>
      </defs>
      <text fill="url(#accent-mono)"><textPath href="#arc-mono" textLength="334">THE GATE TO THE NEW WORLD</textPath></text>
      <path d="M0,68 Q40,60 170,48 Q290,40 354,50 L354,53 Q290,44 170,53 Q60,62 0,74 Z" fill="url(#accent-mono)"/>
    </svg>
    <p class="site">www.WanderNookly.com</p>
    <div class="brand"><span class="brand__dot"></span><span class="brand__name">NOOKLY EVENTS</span></div>
  </section>

</main>
</body>
</html>
```